Android game graphics Hangman

I need graphics for a hangman game for the Android platform.
I am open to anything from a drastic departure from the current styling to a reworking that provides a professional air the game.

I have included screen shots of the current graphics and of my competitors. This project is for the game screen only. Later, another private project will be award to the winner for the design of additional game assets.

Industry/Entity Type

Android

Requirements
Must have
• Visually, I am pretty open to any theme, mass appeal would be best.

Support for English alphabet only at this time.

Space for category listing.

8 errors and you lose. (count not necessary)

Space for a banner Ad.

Design elements that could be used in dialog boxes (see examples of current dialog styling).

```html
<!DOCTYPE html>
<html lang="en">
<head>
<meta charset="utf-8">
<title>Hangman – Game Screen</title>
<link rel="stylesheet" href="https://fonts.googleapis.com/css2?family=Permanent+Marker&family=Gloria+Hallelujah&family=Roboto:wght@400;700&display=swap">
<style>
  :root {
    --page: #ffffff;
    --lime: #d2dc2c;
    --orange: #f7941d;
    --orange-dark: #e0701a;
    --rope: #9a6a3a;
    --red: #e8202a;
    --red-deep: #c41f2e;
    --key-top: #8a8a8a;
    --key-bottom: #3c3c3c;
    --white: #ffffff;
    --ink: #111111;
    --dialog: #eeeeee;
    --miss-red: #e8473a;
    --miss-pale: #f0a59a;
    --miss-grey: #c9c9c9;
    --marker: "Permanent Marker", "Comic Sans MS", "Chalkboard SE", cursive;
    --scrawl: "Gloria Hallelujah", "Comic Sans MS", "Chalkboard SE", cursive;
  }
  * { box-sizing: border-box; margin: 0; padding: 0; }
  html, body { width: 1200px; height: 852px; overflow: hidden; background: var(--page); }
  .board {
    position: relative; width: 706px; height: 500px;
    transform: scale(1.6997); transform-origin: 0 0;
    font-family: "Roboto", Arial, sans-serif;
  }
  .screen {
    position: absolute; top: 10px; width: 302px; height: 480px;
    background: var(--lime); overflow: hidden;
  }
  .screen--playing { left: 42px; }
  .screen--lost { left: 363px; }
  .misses, .gallows { position: absolute; left: 0; top: 0; }
  .character {
    position: absolute; left: 174px; top: 70px; width: 54px; height: 178px;
    border-radius: 10px;
    background: linear-gradient(180deg, #f08a2e 0%, #6f9fc0 55%, #c9403a 100%);
    opacity: 0.9;
  }
  .word-field {
    position: absolute; left: 0; top: 203px; width: 180px; height: 30px;
    background: rgba(255,255,255,0.35); border-radius: 0 4px 4px 0;
  }
  .word-field__text {
    position: absolute; left: 6px; top: 1px;
    font-family: var(--marker); font-weight: 400; font-size: 19px; line-height: 26px;
    color: var(--ink);
  }
  .word-field__line {
    position: absolute; left: 6px; right: 4px; bottom: 6px; height: 1px; background: var(--ink);
  }
  .keyboard {
    position: absolute; left: 8px; top: 303px;
    display: grid; grid-template-columns: repeat(6, 28px); column-gap: 9px; row-gap: 10px;
  }
  .keyboard--bottom-only { top: 382px; }
  .key {
    width: 28px; height: 28px; border-radius: 7px;
    background: linear-gradient(180deg, var(--key-top), var(--key-bottom));
    box-shadow: 0 1px 2px rgba(0,0,0,0.4);
    color: var(--white); font-size: 14px; line-height: 28px; text-align: center;
  }
  .ad-banner {
    position: absolute; left: 0; bottom: 0; width: 100%; height: 38px;
    background: var(--red); color: var(--white);
    font-size: 19px; line-height: 38px; text-align: center;
  }
  .dialog {
    position: absolute; left: 25px; top: 205px; width: 264px; height: 167px;
    background: var(--dialog); border: 5px solid var(--red-deep); border-radius: 14px;
    overflow: hidden;
  }
  .dialog__title {
    position: absolute; left: 14px; top: 8px;
    font-family: var(--scrawl); font-weight: 400; font-size: 25px; line-height: 36px;
    color: var(--red-deep); letter-spacing: 0.5px;
  }
  .dialog__body { position: absolute; left: 9px; top: 62px; color: var(--ink); line-height: 18px; z-index: 1; }
  .dialog__label { font-weight: 700; font-size: 12.5px; }
  .dialog__answer { font-size: 11.5px; }
  .dialog__grave {
    position: absolute; left: 148px; top: 62px; width: 110px; height: 100px;
    background: linear-gradient(180deg, #a0a0a0 0%, #909090 55%, #6fbf3a 85%);
    border-radius: 24px 24px 0 0;
  }
</style>
</head>
<body>
<div class="board">

  <section class="screen screen--playing">
    <svg class="misses" width="140" height="90" viewBox="0 0 140 90" aria-label="Wrong guesses">
      <g stroke="#fff" stroke-width="2.5" stroke-linecap="round">
        <circle cx="15" cy="40" r="11" fill="var(--miss-red)"/><path d="M10 35l10 10M20 35l-10 10"/>
        <circle cx="47" cy="40" r="11" fill="var(--miss-pale)"/><path d="M42 35l10 10M52 35l-10 10"/>
        <circle cx="79" cy="40" r="11" fill="var(--miss-red)"/><path d="M74 35l10 10M84 35l-10 10"/>
        <circle cx="111" cy="40" r="11" fill="var(--miss-red)"/><path d="M106 35l10 10M116 35l-10 10"/>
        <circle cx="15" cy="70" r="11" fill="var(--miss-grey)"/><path d="M10 65l10 10M20 65l-10 10"/>
        <circle cx="47" cy="70" r="11" fill="var(--miss-grey)"/><path d="M42 65l10 10M52 65l-10 10" stroke="#333"/>
        <circle cx="79" cy="70" r="11" fill="var(--miss-pale)"/><path d="M74 65l10 10M84 65l-10 10"/>
        <circle cx="111" cy="70" r="11" fill="var(--miss-red)"/><path d="M106 65l10 10M116 65l-10 10"/>
      </g>
    </svg>
    <svg class="gallows" width="302" height="290" viewBox="0 0 302 290" aria-hidden="true">
      <ellipse cx="210" cy="276" rx="35" ry="5" fill="rgba(0,0,0,0.25)"/>
      <path d="M198 24H262a8 8 0 0 1 8 8V252" fill="none" stroke="var(--orange)" stroke-width="12"/>
      <rect x="196" y="24" width="10" height="48" fill="var(--rope)"/>
      <rect x="246" y="248" width="46" height="32" rx="4" fill="var(--orange-dark)"/>
    </svg>
    <div class="word-field">
      <span class="word-field__text">THE WORD</span>
      <span class="word-field__line"></span>
    </div>
    <div class="character" role="img" aria-label="Illustration area: cartoon character hanging from the rope"></div>
    <div class="keyboard">
      <span class="key">A</span><span class="key">A</span><span class="key">A</span><span class="key">A</span><span class="key">A</span><span class="key">A</span>
      <span class="key">A</span><span class="key">A</span><span class="key">A</span><span class="key">A</span><span class="key">A</span><span class="key">A</span>
      <span class="key">A</span><span class="key">A</span><span class="key">A</span><span class="key">A</span><span class="key">A</span><span class="key">A</span>
    </div>
    <div class="ad-banner">Ad Place Holder</div>
  </section>

  <section class="screen screen--lost">
    <svg class="misses" width="140" height="90" viewBox="0 0 140 90" aria-label="Wrong guesses">
      <g stroke="#fff" stroke-width="2.5" stroke-linecap="round">
        <circle cx="15" cy="40" r="11" fill="var(--miss-red)"/><path d="M10 35l10 10M20 35l-10 10"/>
        <circle cx="47" cy="40" r="11" fill="var(--miss-pale)"/><path d="M42 35l10 10M52 35l-10 10"/>
        <circle cx="79" cy="40" r="11" fill="var(--miss-red)"/><path d="M74 35l10 10M84 35l-10 10"/>
        <circle cx="111" cy="40" r="11" fill="var(--miss-red)"/><path d="M106 35l10 10M116 35l-10 10"/>
        <circle cx="15" cy="70" r="11" fill="var(--miss-grey)"/><path d="M10 65l10 10M20 65l-10 10"/>
        <circle cx="47" cy="70" r="11" fill="var(--miss-grey)"/><path d="M42 65l10 10M52 65l-10 10" stroke="#333"/>
        <circle cx="79" cy="70" r="11" fill="var(--miss-pale)"/><path d="M74 65l10 10M84 65l-10 10"/>
        <circle cx="111" cy="70" r="11" fill="var(--miss-red)"/><path d="M106 65l10 10M116 65l-10 10"/>
      </g>
    </svg>
    <svg class="gallows" width="302" height="290" viewBox="0 0 302 290" aria-hidden="true">
      <path d="M198 24H262a8 8 0 0 1 8 8V252" fill="none" stroke="var(--orange)" stroke-width="12"/>
      <rect x="196" y="24" width="10" height="48" fill="var(--rope)"/>
      <rect x="246" y="248" width="46" height="32" rx="4" fill="var(--orange-dark)"/>
    </svg>
    <div class="word-field">
      <span class="word-field__text">T</span>
    </div>
    <div class="character" role="img" aria-label="Illustration area: sad cartoon character hanging from the rope"></div>
    <div class="keyboard keyboard--bottom-only">
      <span class="key">A</span><span class="key">A</span><span class="key">A</span><span class="key">A</span><span class="key">A</span><span class="key">A</span>
    </div>
    <div class="dialog" role="dialog" aria-label="Game over">
      <h2 class="dialog__title">GAME OVER</h2>
      <div class="dialog__grave" role="img" aria-label="Illustration area: gravestone on grass"></div>
      <div class="dialog__body">
        <p class="dialog__label">The word was</p>
        <p class="dialog__answer">THE ANSWER</p>
        <p class="dialog__label">Losing streak of : 3</p>
      </div>
    </div>
    <div class="ad-banner">Ad Place Holder</div>
  </section>

</div>
</body>
</html>
```